TM Holdings-Homes for Tomorrow's World

TM Holdings is a Residential Real Estate company which specializes in buying and selling homes. We pride ourselves on service, expertise, and building relationships. I would like to do a Billboard Ad for a The Size is 14 feet (Height) x 48 feet (width) displaying our current motto for "Real Estate of the Future" We have launched new programs and working with leaders in our industy Pavrit and other tech companies and changing the way Real Estate is done in Las Vegas, NV. Its exciting and NEW so we want to get the word out. Color Scheme Red, White, Grey and maybe black. Logo is uploaded and so is a picture head shot. I would like to see options with my headshot and with out.

```html
<!DOCTYPE html>
<html lang="en">
<head>
<meta charset="utf-8">
<title>TM Holdings Billboard</title>
<link href="https://fonts.googleapis.com/css2?family=Anton&family=Open+Sans:wght@400;600;800&display=swap" rel="stylesheet">
<style>
  :root {
    --page-bg: #ececec;
    --white: #ffffff;
    --brand-red: #b50d0d;
    --deep-red: #6e0606;
    --ink: #222222;
    --photo-green: #5f7a3e;
    --photo-leaf: #7d9452;
    --photo-dark: #34422a;
    --photo-warm: #a3916a;
    --photo-navy: #27324a;
  }
  html, body {
    margin: 0;
    padding: 0;
    width: 1079px;
    height: 1200px;
    overflow: hidden;
    background: var(--page-bg);
  }
  .canvas {
    width: 1079px;
    height: 1200px;
    display: flex;
    align-items: center;
    justify-content: center;
  }
  .billboard {
    width: 1019px;
    height: 297px;
    display: flex;
    box-shadow: 0 6px 18px rgba(0,0,0,0.25);
  }
  .billboard-message {
    width: 611px;
    background: var(--white);
    display: flex;
    flex-direction: column;
  }
  .brand-bar {
    height: 96px;
    display: flex;
    align-items: center;
    justify-content: center;
  }
  .brand-name {
    font-family: "Open Sans", sans-serif;
    font-weight: 600;
    font-size: 40px;
    letter-spacing: 3px;
    color: var(--brand-red);
    text-transform: uppercase;
  }
  .headline-band {
    height: 132px;
    background: linear-gradient(110deg, var(--deep-red) 0%, var(--brand-red) 35%, var(--brand-red) 70%, #8c0909 100%);
    display: flex;
    flex-direction: column;
    align-items: center;
    justify-content: center;
    color: var(--white);
  }
  .headline {
    font-family: "Anton", sans-serif;
    font-weight: 400;
    font-size: 45px;
    line-height: 1.1;
    text-transform: uppercase;
    margin: 0;
    letter-spacing: 0.5px;
  }
  .phone {
    font-family: "Open Sans", sans-serif;
    font-weight: 800;
    font-size: 40px;
    line-height: 1.1;
    margin: 2px 0 0;
  }
  .contact-bar {
    flex: 1;
    display: flex;
    flex-direction: column;
    align-items: center;
    justify-content: center;
    font-family: "Open Sans", sans-serif;
    color: var(--ink);
  }
  .address {
    font-size: 12px;
    margin: 0 0 2px;
  }
  .website {
    font-size: 19px;
    margin: 0;
  }
  .website .domain {
    color: var(--brand-red);
    font-weight: 600;
  }
  .headshot {
    flex: 1;
    background:
      linear-gradient(180deg, rgba(39,50,74,0) 0%, rgba(39,50,74,0) 55%, rgba(39,50,74,0.55) 100%),
      linear-gradient(90deg, var(--photo-dark) 0%, var(--photo-green) 25%, var(--photo-leaf) 50%, var(--photo-green) 75%, var(--photo-warm) 100%);
  }
</style>
</head>
<body>
<main class="canvas">
  <section class="billboard">
    <div class="billboard-message">
      <header class="brand-bar">
        <span class="brand-name">TM Holdings</span>
      </header>
      <div class="headline-band">
        <h1 class="headline">Homes for Tomorrow's World</h1>
        <p class="phone">702-555-0148</p>
      </div>
      <footer class="contact-bar">
        <p class="address">218 W Sunridge Ave Ste 40, Henderson, NV, 89012</p>
        <p class="website">www.<span class="domain">tmholdingsgroup</span>.net</p>
      </footer>
    </div>
    <div class="headshot" role="img" aria-label="Headshot photo of the agent in a dark blazer and blue shirt, in a garden with a tree and pink flowers"></div>
  </section>
</main>
</body>
</html>
```